Fintech company needs ads created around "can't afford help"

Design 3 ads (total) that focus around HELPING people who can't afford to get help with their finances.

The 3 ads will be made up of 1 design for each audience:
• Millennial
• Generation X
• Baby Boomer

We are testing campaigns in Chatterloop that will drive to a landing page. We are an online financial-tech company who helps people manage their retirement account. We’re looking for creative talent who are effective at developing imagery to be used in Chatterloop to grab people’s attention and drive clicks. Because of the scrutiny in our industry, we’ll handle the ad copy above and below the imagery you create. We encourage you to use/not use words in your creative.

Target Market(s)

• Millennial
• Generation X
• Baby Boomer

Industry/Entity Type

Financial Service

Requirements
Must have
• Image Dimensions
• Width: 1200 Height: 628
• Final PSD Designs
• Feel free to play around with any color scheme.
• Tasteful – we are not a traditional, stodgy Wall Street Financial firm, but we need to convey that we are trustworthy and legitimate.
Nice to have
• You are not limited to photos – whatever you believe will stand out and engage with prospective clients is fair game (including illustrations, animation, video, etc).
• Think about how your work could translate into other forms such as motion graphics or video.
• Ultimately, we will test our favorites and come back to those with the highest performance which will turn into additional work and additional formats.
Should not have
• • No stock photography UNLESS found at Pixvarra (we will pay for the image)
• • No Testimonials – regulations prevent us from using testimonials in our advertisements

```html
<!DOCTYPE html>
<html lang="en">
<head>
<meta charset="utf-8">
<title>Live Life to the Fullest – Retirement Ad</title>
<link rel="stylesheet" href="https://fonts.googleapis.com/css2?family=Roboto:wght@300;400;500&family=Russo+One&display=swap">
<style>
  :root {
    --page: #ffffff;
    --ad-dark: #110c0b;
    --ad-dark-2: #1b1615;
    --shirt-blue: #5d9fd6;
    --shirt-deep: #2f6fae;
    --skin: #c9917a;
    --yellow: #f6ec15;
    --white: #ffffff;
    --green: #3c9a17;
    --green-light: #58b825;
    --green-dark: #226b0a;
    --brand-blue: #0d4c8c;
    --fold-light: #f4f4f4;
    --fold-shadow: #9a9a9a;
  }
  html, body {
    margin: 0;
    padding: 0;
    width: 1200px;
    height: 1200px;
    overflow: hidden;
    background: var(--page);
  }
  .canvas {
    position: relative;
    width: 1200px;
    height: 1200px;
    background: var(--page);
  }
  .ad {
    position: absolute;
    left: 0;
    top: 286px;
    width: 1200px;
    height: 628px;
    overflow: hidden;
    background: linear-gradient(90deg, var(--ad-dark) 0%, var(--ad-dark) 40%, var(--ad-dark-2) 100%);
    font-family: "Roboto", Arial, sans-serif;
  }
  .hero-photo {
    position: absolute;
    left: 420px;
    top: 0;
    width: 620px;
    height: 628px;
    background:
      radial-gradient(ellipse 26% 22% at 52% 30%, var(--skin) 0%, rgba(201,145,122,0.55) 55%, rgba(201,145,122,0) 100%),
      radial-gradient(ellipse 55% 50% at 52% 85%, var(--shirt-blue) 0%, var(--shirt-deep) 55%, rgba(47,111,174,0) 100%);
  }
  .headline {
    position: absolute;
    left: 89px;
    top: 96px;
    margin: 0;
    color: var(--yellow);
    font-weight: 300;
  }
  .headline-lead {
    display: block;
    font-size: 56px;
    line-height: 60px;
    letter-spacing: 0.5px;
  }
  .headline-lead .soft {
    color: var(--white);
  }
  .headline-shout {
    display: block;
    margin-top: 4px;
    font-family: "Russo One", Impact, sans-serif;
    font-size: 88px;
    line-height: 84px;
    letter-spacing: 3px;
  }
  .pitch {
    position: absolute;
    left: 89px;
    top: 246px;
    margin: 0;
    color: var(--white);
    font-size: 30px;
    line-height: 35px;
    font-weight: 400;
  }
  .cta {
    position: absolute;
    left: 86px;
    top: 446px;
    width: 370px;
    height: 86px;
    border-radius: 4px;
    background: linear-gradient(180deg, var(--green-light) 0%, var(--green) 55%, var(--green) 88%, var(--green-dark) 88%, var(--green-dark) 100%);
    display: flex;
    align-items: center;
    justify-content: center;
    gap: 16px;
    color: var(--white);
    font-size: 42px;
    font-weight: 400;
    padding-bottom: 8px;
    box-sizing: border-box;
  }
  .cta-icon {
    width: 52px;
    height: 52px;
  }
  .page-curl {
    position: absolute;
    left: 0;
    top: 0;
  }
  .logo-note {
    position: absolute;
    left: 1094px;
    top: 484px;
    color: var(--brand-blue);
    font-size: 15px;
    font-weight: 400;
  }
  .brand-name {
    position: absolute;
    left: 1072px;
    top: 546px;
    color: var(--brand-blue);
    font-size: 26px;
    font-weight: 500;
  }
</style>
</head>
<body>
  <div class="canvas">
    <section class="ad">
      <div class="hero-photo" role="img" aria-label="Photo of a cheerful senior man in a light blue shirt clenching his fists in celebration"></div>

      <h1 class="headline">
        <span class="headline-lead">LIVE LIFE <span class="soft">to the</span></span>
        <span class="headline-shout">FULLEST!</span>
      </h1>

      <p class="pitch">We help handing your<br>finances and manage<br>your retirement account.</p>

      <div class="cta">
        <span>learn more</span>
        <svg class="cta-icon" viewBox="0 0 52 52" aria-hidden="true">
          <circle cx="26" cy="26" r="24" fill="#ffffff"/>
          <path d="M20 14 L38 26 L20 38 Z" fill="#2f8a12"/>
        </svg>
      </div>

      <svg class="page-curl" width="1200" height="628" viewBox="0 0 1200 628" aria-hidden="true">
        <defs>
          <linearGradient id="foldShade" x1="0" y1="0" x2="1" y2="1">
            <stop offset="0" stop-color="#ffffff"/>
            <stop offset="0.55" stop-color="#e6e6e6"/>
            <stop offset="1" stop-color="#9a9a9a"/>
          </linearGradient>
        </defs>
        <path d="M960 628 C1060 560 1150 470 1200 356 L1200 628 Z" fill="#ffffff"/>
        <path d="M1200 356 C1170 430 1120 470 1090 520 C1060 570 1020 605 960 628 C1040 600 1085 540 1120 480 C1150 430 1180 390 1200 356 Z" fill="url(#foldShade)"/>
      </svg>

      <span class="logo-note">logo here</span>
      <span class="brand-name">Ledgerly</span>
    </section>
  </div>
</body>
</html>
```